Your complete Gardening and lawn maintenance, Horticultural care. (to be on card)
We are looking at using a logo of a tree, with a recycling emblem circling the tree. The colors of choice, are burnt oranges and olive greens. Presented; simple to the eye, yet catchy to the clients in a eco-friendly way. We have uploaded a design for you to look at just to give a rough idea, you can use that or create your own ideas or play around with a mixture.

Target Market(s)

Home owners, businesses, real estates.

Industry/Entity Type

Recycling

Contact Information for Business Card

Name: Colin Breversted
Phone: 0438159027
Email: brightmossyards@mailbarn.net

Logo Text

Bright-Moss Yards

Logo styles of interest
Emblem Logo
Pictorial/Combination Logo
Abstract Logo
Requirements
Must have
• Business name: Bright-Moss Yards
and slogan : Your complete Gardening and lawn maintenance, Horticultural care

```html
<!DOCTYPE html>
<html lang="en">
<head>
<meta charset="utf-8">
<title>Bright-Moss Yards — Business Card</title>
<link rel="stylesheet" href="https://fonts.googleapis.com/css2?family=Arimo:wght@400;700&display=swap">
<style>
  :root {
    --backdrop: #3a3a3a;
    --card-cream: #e9e2a6;
    --card-cream-edge: #ddd596;
    --burnt-orange: #c8621e;
    --name-orange: #c25a1a;
    --olive: #9aa23a;
    --olive-dark: #4b4a1c;
    --ink: #3e3a22;
    --band-highlight: #e3dc7a;
    --band-text: #efe6b4;
  }
  * { box-sizing: border-box; margin: 0; padding: 0; }
  html, body {
    width: 1200px;
    height: 1000px;
    overflow: hidden;
    background: var(--backdrop);
    font-family: "Arimo", Arial, sans-serif;
  }
  .canvas {
    position: relative;
    width: 1200px;
    height: 1000px;
    display: flex;
    align-items: center;
    justify-content: center;
  }
  .business-card {
    position: relative;
    width: 1000px;
    height: 572px;
    background: radial-gradient(ellipse at 40% 40%, var(--card-cream) 55%, var(--card-cream-edge) 100%);
    overflow: hidden;
  }
  .contact {
    position: absolute;
    top: 48px;
    right: 60px;
    text-align: right;
    color: var(--ink);
  }
  .contact__name {
    font-size: 52px;
    letter-spacing: 0.5px;
    color: var(--name-orange);
    font-weight: 400;
    line-height: 1;
  }
  .contact__name strong { font-weight: 700; }
  .contact__line {
    font-size: 26px;
    margin-top: 14px;
  }
  .contact__line b { font-weight: 700; margin-right: 6px; }
  .contact__line--email { margin-top: 30px; margin-right: 40px; }
  .brand {
    position: absolute;
    left: 70px;
    top: 270px;
    display: flex;
    align-items: center;
    gap: 34px;
  }
  .brand__dot {
    width: 170px;
    height: 170px;
    flex: none;
  }
  .brand__name {
    font-size: 66px;
    font-weight: 700;
    color: var(--olive-dark);
    line-height: 1;
    letter-spacing: 0.5px;
  }
  .slogan-band {
    position: absolute;
    left: 0;
    right: 0;
    bottom: 0;
    height: 96px;
    background: var(--burnt-orange);
    display: flex;
    align-items: center;
    padding-left: 40px;
    font-size: 27px;
    color: var(--band-text);
    white-space: nowrap;
  }
  .slogan-band strong { color: var(--band-highlight); font-weight: 700; }
</style>
</head>
<body>
<main class="canvas">
  <article class="business-card">
    <section class="contact">
      <h1 class="contact__name"><strong>COLIN</strong> BREVERSTED</h1>
      <p class="contact__line"><b>P</b>0438159027</p>
      <p class="contact__line contact__line--email"><b>E</b>brightmossyards@mailbarn.net</p>
    </section>

    <div class="brand">
      <svg class="brand__dot" viewBox="0 0 170 170" aria-hidden="true">
        <circle cx="85" cy="85" r="85" fill="var(--olive)"/>
      </svg>
      <span class="brand__name">Bright-Moss Yards</span>
    </div>

    <footer class="slogan-band">
      <p>complete <strong>gardening</strong> &amp; <strong>lawn maintenance</strong> &amp; <strong>horticultural</strong> care</p>
    </footer>
  </article>
</main>
</body>
</html>
```